Velimo Ventures Logo and Business Card Design

We already have the rough logo shape (however please make the lines on the logo much thicker so a dark background is not required to see it) . see photos uploaded.
It needs to be refined with color and digitized and then have a front and back business card layout done.
The services are high vibration healing support through a therapy and feng shui service offering. We want people to Feel Happiness, Feel Prosperity and Feel Peace. (the back of the card would have these phrases on it) So a warm, calm and peaceful feeling card.
We would like the card to use the logo provided (with thicker lines and color added) but below the graphic please use the name "Velimo Ventures" NOT Velimo.
We also would like to use the colors in the colorized matrix shown in photos (gold and purple) but on the lighter side. Thanks for your time!

Front of Card should include: Logo, with Company Name: Velimo Ventures as part of logo, Name: Mara Donne email: mara@velimo.example web: www.velimo.example mobile: 555.018.2946 at bottom of front list Family Constellation | Feng Shui

Back of Card should have the logo and the following listed vertically:

PERSONAL | BUSINESS (Larger size then smaller bullet items below)
*Find Happiness
*Find Prosperity
*Find Peace

Target Market(s)

Target market is both business and personal

Contact Information for Business Card

Front of Card should include: Logo, with Company Name: Velimo Ventures as part of logo, Name: Mara Donne email: mara@velimo.example web: www.velimo.example mobile: 555.018.2946 at bottom of front list Family Constellation | Feng Shui ++++ Back of Card should have the logo and the following listed vertically: PERSONAL | BUSINESS (Larger size then smaller bullet items below) *Find Happiness *Find Prosperity *Find Peace

Font styles to use
Sans Serif

Colors

Designer to choose colors to be used in the design.

Requirements
Nice to have
• Nice light contrast color for the back of card background
Should not have
• No dark colored background on Card.

```html
<!DOCTYPE html>
<html lang="en">
<head>
<meta charset="utf-8">
<title>Velimo Ventures – Business Card</title>
<link rel="stylesheet" href="https://fonts.googleapis.com/css2?family=Montserrat:wght@400;500;700&display=swap">
<style>
  :root {
    --navy: #20205e;
    --red: #e31c25;
    --white: #ffffff;
    --ink: #2a2a3a;
    --back-tint: #eceaf7;
    --bullet: #8c86c4;
    --stage: #e9e9ee;
  }
  * { margin: 0; padding: 0; box-sizing: border-box; }
  html, body { width: 1200px; height: 988px; overflow: hidden; }
  body {
    background: var(--stage);
    font-family: "Montserrat", Arial, sans-serif;
    position: relative;
  }
  .card {
    position: absolute;
    width: 620px;
    height: 354px;
    border-radius: 22px;
    overflow: hidden;
    box-shadow: 0 6px 18px rgba(32, 32, 94, .12);
  }
  .brand {
    display: flex;
    align-items: center;
    gap: 14px;
    color: var(--red);
    font-weight: 700;
    letter-spacing: 1px;
    text-transform: uppercase;
    white-space: nowrap;
  }
  .brand-dot {
    flex: none;
    border: 4px solid var(--red);
    border-radius: 50%;
  }
  .bullet {
    flex: none;
    width: 9px; height: 9px;
    border-radius: 50%;
    border: 1.5px solid var(--bullet);
  }

  /* Back side */
  .card-back {
    left: 60px; top: 70px;
    background: var(--back-tint);
    color: var(--navy);
    display: flex;
    flex-direction: column;
    align-items: center;
    justify-content: center;
  }
  .card-back .brand { font-size: 34px; justify-content: center; }
  .card-back .brand-dot { width: 40px; height: 40px; }
  .audience {
    margin-top: 24px;
    padding: 0 20px 6px;
    color: var(--red);
    font-size: 16px;
    font-weight: 500;
    letter-spacing: 1px;
    border-bottom: 2px solid var(--red);
  }
  .promises {
    display: flex;
    justify-content: center;
    gap: 22px;
    margin-top: 20px;
    list-style: none;
    font-size: 14px;
    font-weight: 500;
    letter-spacing: .5px;
  }
  .promises li { display: flex; align-items: center; gap: 8px; }

  /* Front side */
  .card-front {
    left: 520px; top: 560px;
    background: var(--white);
    color: var(--ink);
  }
  .edge-mark {
    position: absolute;
    left: 0; top: 56px;
    width: 16px; height: 40px;
    background: var(--navy);
  }
  .holder { position: absolute; left: 40px; top: 44px; }
  .holder-name { color: var(--red); font-size: 30px; font-weight: 700; line-height: 1; }
  .holder-role { font-size: 14px; font-weight: 500; margin-top: 4px; }
  .rule { width: 14px; height: 2px; background: var(--navy); margin: 18px 0 14px; }
  .contacts, .services { list-style: none; font-size: 14px; line-height: 1.55; }
  .contacts li, .services li { display: flex; align-items: center; gap: 8px; }
  .contacts svg { width: 12px; height: 12px; fill: var(--red); flex: none; }
  .services .bullet { border-color: var(--navy); }
  .card-front .brand {
    position: absolute;
    right: 34px; top: 120px;
    font-size: 26px;
  }
  .card-front .brand-dot { width: 32px; height: 32px; }
  .footer-bands { position: absolute; left: 0; bottom: 0; width: 620px; height: 90px; }
</style>
</head>
<body>

  <section class="card card-back" aria-label="Back of business card">
    <div class="brand"><span class="brand-dot"></span>Velimo Ventures</div>
    <div class="audience">PERSONAL | BUSINESS</div>
    <ul class="promises">
      <li><span class="bullet"></span>Find Happiness</li>
      <li><span class="bullet"></span>Find Prosperity</li>
      <li><span class="bullet"></span>Find Peace</li>
    </ul>
  </section>

  <section class="card card-front" aria-label="Front of business card">
    <span class="edge-mark"></span>
    <div class="holder">
      <p class="holder-name">Mara Donne</p>
      <p class="holder-role">Owner</p>
      <div class="rule"></div>
      <ul class="contacts">
        <li><svg viewBox="0 0 12 12" aria-hidden="true"><path d="M2 1h3l1 3-1.5 1a6 6 0 0 0 2.5 2.5L8 6l3 1v3a1 1 0 0 1-1 1A9 9 0 0 1 1 2a1 1 0 0 1 1-1z"/></svg>555.018.2946</li>
        <li><svg viewBox="0 0 12 12" aria-hidden="true"><path d="M1 2.5h10v7H1z M1 2.5l5 4 5-4" fill="none" stroke="#e31c25" stroke-width="1.4"/></svg>mara@velimo.example</li>
        <li><svg viewBox="0 0 12 12" aria-hidden="true"><circle cx="6" cy="6" r="5" fill="none" stroke="#e31c25" stroke-width="1.4"/><path d="M1 6h10M6 1c-2.5 3-2.5 7 0 10M6 1c2.5 3 2.5 7 0 10" fill="none" stroke="#e31c25" stroke-width="1"/></svg>www.velimo.example</li>
      </ul>
      <div class="rule"></div>
      <ul class="services">
        <li><span class="bullet"></span>Feng Shui</li>
        <li><span class="bullet"></span>Family Constellation</li>
      </ul>
    </div>
    <div class="brand"><span class="brand-dot"></span>Velimo Ventures</div>
    <svg class="footer-bands" viewBox="0 0 620 90" preserveAspectRatio="none" aria-hidden="true">
      <polygon points="0,72 420,34 420,90 0,90" fill="#e31c25"/>
      <polygon points="428,33 620,16 620,90 428,90" fill="#20205e"/>
    </svg>
  </section>

</body>
</html>
```